Tasman Curdworks Guild needs new business cards

We need new business cards designed and produced. We are likely to need other design work done for ads, flyers etc in future.

We would like to start with an initial business card.

The Tasman Curdworks Guild (TCG) is a membership-based not-for-profit organisation that looks after the interests of Australia's small to medium artisan cheesemakers, many of whom are also small-scale farmers. The design should be simple, using our logo, but also communicate our artisan cheese and small dairy farm focus.

The first card to be designed and produced is for me, Miriam Tolhurst. My details are:

Miriam Tolhurst
Secretary
Tasman Curdworks Guild (TCG)
http://www.curdworksguild.example
T +61452837190
E miriam.miriamtolhurst@mailbox.example

I have attached the TCG logo in jpg form. I have a higher resolution version available if needed.

Thank you!

Miriam

Miriam Tolhurst
Tasman Curdworks Guild
miriam.miriamtolhurst@mailbox.example
+61452837190

Sans Serif

• Logo (see attached file)

```html
<!DOCTYPE html>
<html lang="en">
<head>
<meta charset="utf-8">
<title>Tasman Curdworks Guild — Business Card</title>
<link rel="stylesheet" href="https://fonts.googleapis.com/css2?family=Cormorant+Garamond:wght@500&family=Open+Sans:wght@400;600&display=swap">
<style>
  :root {
    --card: #ffffff;
    --brand-brown: #5a2e1c;
    --ink: #1c1c1c;
    --cheese: #f3b63f;
    --cheese-pale: #fde6bd;
    --rind-line: #b9a597;
  }
  * { box-sizing: border-box; margin: 0; padding: 0; }
  html, body {
    width: 1200px;
    height: 716px;
    overflow: hidden;
    background: var(--card);
  }
  .business-card {
    position: relative;
    width: 1200px;
    height: 716px;
    background: var(--card);
    font-family: "Open Sans", Arial, sans-serif;
    color: var(--ink);
  }
  .brand {
    position: absolute;
    left: 96px;
    top: 64px;
    display: flex;
    align-items: flex-start;
    gap: 34px;
  }
  .brand-dot {
    width: 74px;
    height: 74px;
    border-radius: 50%;
    background: var(--cheese);
    margin-top: 8px;
    flex-shrink: 0;
  }
  .brand-name {
    font-family: "Cormorant Garamond", Georgia, serif;
    font-weight: 500;
    font-size: 44px;
    line-height: 40px;
    letter-spacing: 1px;
    color: var(--brand-brown);
  }
  .brand-name span { display: block; }
  .brand-name span:nth-child(2) { padding-left: 18px; }
  .brand-name span:nth-child(3) { padding-left: 36px; }
  .person {
    position: absolute;
    left: 96px;
    top: 236px;
  }
  .person-name {
    font-weight: 600;
    font-size: 27px;
    line-height: 32px;
  }
  .person-role {
    font-size: 16px;
    line-height: 20px;
  }
  .contact {
    position: absolute;
    left: 96px;
    top: 318px;
    list-style: none;
    font-size: 20px;
    line-height: 27px;
  }
  .contact .phone { margin-bottom: 34px; }
  .cheese-art {
    position: absolute;
    right: 70px;
    bottom: 60px;
    width: 290px;
    height: 220px;
    border-radius: 46% 46% 8px 8px;
    background: radial-gradient(circle at 50% 42%, var(--cheese-pale) 0 55%, #f6e9de 75%, var(--card) 100%);
  }
</style>
</head>
<body>
  <main class="business-card">
    <header class="brand">
      <div class="brand-dot"></div>
      <h1 class="brand-name"><span>Tasman</span><span>Curdworks</span><span>Guild</span></h1>
    </header>

    <section class="person">
      <p class="person-name">Miriam Tolhurst</p>
      <p class="person-role">Secretary</p>
    </section>

    <ul class="contact">
      <li class="phone">61452837190</li>
      <li class="web">www.curdworksguild.example</li>
      <li class="email">miriam.miriamtolhurst@mailbox.example</li>
    </ul>

    <div class="cheese-art" role="img" aria-label="Decorative cheese wheel illustration in pale gold with a thin rind outline"></div>
  </main>
</body>
</html>
```